Veradine Contracting Folder

Creating a design for the cover of our folders that we pass to our customers

Want to keep the same look as our colors and fonts as attached

```html
<!DOCTYPE html>
<html lang="en">
<head>
<meta charset="utf-8">
<title>Veradine Contracting Folder</title>
<link href="https://fonts.googleapis.com/css2?family=Questrial&family=Arimo:wght@400;700&display=swap" rel="stylesheet">
<style>
  :root {
    --royal: #0d0fa6;
    --royal-deep: #08098a;
    --lavender: #aaaadf;
    --gold: #e6c43a;
    --gold-light: #f5d85a;
    --paper: #f4f4f4;
    --pattern: #eeece4;
    --backdrop: #b4b4b4;
  }
  * { box-sizing: border-box; margin: 0; padding: 0; }
  html, body { width: 842px; height: 1200px; overflow: hidden; }
  body { background: var(--backdrop); font-family: "Questrial", sans-serif; position: relative; }

  .spread { position: absolute; left: 41px; width: 760px; display: flex; box-shadow: 0 8px 24px rgba(0,0,0,.25); }
  .spread--outer { top: 40px; height: 520px; }
  .spread--inner { top: 610px; height: 550px; }
  .panel { position: relative; width: 380px; height: 100%; overflow: hidden; }

  /* back cover */
  .back-cover { background: linear-gradient(160deg, var(--royal) 0%, var(--royal-deep) 100%); }
  .watermark { position: absolute; left: 0; right: 0; top: 170px; text-align: center; color: rgba(255,255,255,.09); }
  .watermark .wordmark-name { font-size: 52px; letter-spacing: 2px; }
  .watermark .wordmark-sub { font-size: 24px; letter-spacing: 6px; }
  .contact-band { position: absolute; left: 0; right: 0; top: 420px; height: 64px; background: var(--paper); border-top: 2px solid var(--lavender); border-bottom: 2px solid var(--gold); padding: 12px 16px; font-family: "Arimo", sans-serif; color: var(--royal); font-size: 8px; line-height: 14px; text-align: center; }
  .contact-band strong { font-weight: 700; }
  .contact-item { display: inline-flex; align-items: center; gap: 3px; margin: 0 4px; }
  .contact-item svg { width: 8px; height: 8px; fill: var(--royal); }

  /* front cover */
  .front-cover { background: linear-gradient(135deg, #ffffff 40%, #e6e6e6 100%); }
  .wordmark { position: absolute; left: 0; right: 0; top: 150px; display: flex; justify-content: center; align-items: center; gap: 12px; color: var(--royal); }
  .wordmark-mark { width: 10px; height: 10px; background: var(--gold); }
  .wordmark-text { text-align: center; }
  .wordmark-name { display: block; font-size: 46px; letter-spacing: 1px; line-height: 1; }
  .wordmark-sub { display: block; font-size: 22px; letter-spacing: 5px; margin-top: 6px; }
  .web-band { position: absolute; left: 0; right: 0; top: 395px; height: 44px; background: var(--royal); border-top: 2px solid var(--lavender); display: flex; align-items: center; justify-content: center; color: #fff; font-size: 12px; letter-spacing: 3px; }
  .web-rule { position: absolute; left: 0; right: 0; top: 446px; height: 2px; background: var(--gold); }

  /* inside */
  .inside { background: var(--paper); }
  .inside-pattern { position: absolute; inset: 0; background: var(--pattern); }
  .pocket { position: absolute; left: 0; right: 0; top: 330px; bottom: 0; background: linear-gradient(160deg, var(--gold-light), var(--gold)); box-shadow: 0 -3px 8px rgba(0,0,0,.12); }
  .card-slit { position: absolute; background: rgba(60,50,10,.55); }
  .card-slit--h { width: 14px; height: 1px; }
  .card-slit--v { width: 1px; height: 14px; }
  .pocket .wordmark { top: 105px; gap: 8px; }
  .pocket .wordmark-name { font-size: 30px; }
  .pocket .wordmark-sub { font-size: 14px; letter-spacing: 3px; margin-top: 3px; }
  .fold { position: absolute; top: 0; bottom: 0; left: 380px; width: 1px; background: rgba(0,0,0,.1); }
</style>
</head>
<body>

<section class="spread spread--outer">
  <div class="panel back-cover">
    <div class="watermark">
      <span class="wordmark-name">Veradine</span>
      <span class="wordmark-sub">Contracting</span>
    </div>
    <div class="contact-band">
      <strong>Veradine Contracting Ltd,</strong> 42 Harbor View Road, Marlow Bay, Alaska 34512<br>
      <span class="contact-item"><svg viewBox="0 0 10 10"><path d="M2 1l2 2-1 1.5c.8 1.5 1.5 2.2 3 3L7.5 6l2 2-1.5 1.5C4 9 1 6 .5 1.5z"/></svg>555 014 2538</span>
      <span class="contact-item"><svg viewBox="0 0 10 10"><path d="M3 0h4v10H3zM4 1v7h2V1z"/></svg>555 018 9364</span>
      <span class="contact-item"><svg viewBox="0 0 10 10"><path d="M2 0h6v3H2zM0 4h10v5H0z"/></svg>555 012 1940</span>
      <span class="contact-item"><svg viewBox="0 0 10 10"><path d="M0 2h10v6H0zM1 3l4 3 4-3"/></svg>info@veradinecontracting.com</span>
    </div>
  </div>
  <div class="panel front-cover">
    <div class="wordmark">
      <span class="wordmark-mark"></span>
      <span class="wordmark-text">
        <span class="wordmark-name">Veradine</span>
        <span class="wordmark-sub">Contracting</span>
      </span>
    </div>
    <div class="web-band">www.veradinecontracting.com</div>
    <div class="web-rule"></div>
  </div>
</section>

<section class="spread spread--inner">
  <div class="panel inside">
    <div class="inside-pattern" role="img" aria-label="Pale gold and grey striped background pattern"></div>
    <div class="pocket">
      <span class="card-slit card-slit--h" style="left:50px;top:40px"></span>
      <span class="card-slit card-slit--v" style="left:150px;top:70px"></span>
      <span class="card-slit card-slit--h" style="left:90px;top:115px"></span>
    </div>
  </div>
  <div class="panel inside">
    <div class="inside-pattern" role="img" aria-label="Pale gold and grey striped background pattern"></div>
    <div class="pocket">
      <div class="wordmark">
        <span class="wordmark-mark"></span>
        <span class="wordmark-text">
          <span class="wordmark-name">Veradine</span>
          <span class="wordmark-sub">Contracting</span>
        </span>
      </div>
    </div>
  </div>
  <div class="fold"></div>
</section>

</body>
</html>
```